Bramford Holloway Inc. needs an innovative idea for letterhead and visiting cards.

Bramford Holloway Inc. is a Canadian brand since 2007. It is a renown dealer of kids and office furniture locally. Moreover, exporting electric fixtures e.g. switches, LED's, down-lights etc. to Middle East and Africa. We have initiated a number of steps including re-branding, to boost our export in 2020. We have successfully designed our new logo a few months ago through 'Mockplanet' and now we are looking for an innovative idea for a letterhead.
Some key points:
• Red, black and white are the three colors used in all our packaging and furniture. (grey is optional)
• Shouldn’t be too wide.
• Use of watermark is preferable.
• You can visit our North American site at www.bramfordhollowayinc.com. Export website of the company will be launched soon. www.bramfordhollowayinc.ca
• Same letterhead will be used locally and internationally.
• Our new logo and sample packaging is attached.

```html
<!DOCTYPE html>
<html lang="en">
<head>
<meta charset="utf-8">
<title>Bramford Holloway Inc. Letterhead</title>
<link href="https://fonts.googleapis.com/css2?family=Questrial&family=Open+Sans:wght@600&family=Noto+Serif&display=swap" rel="stylesheet">
<style>
  :root {
    --brand-red: #8a1014;
    --ink-black: #111111;
    --paper: #ffffff;
    --watermark: #efdfd7;
    --tagline-grey: #3a3a3a;
    --page-edge: #e4e4e4;
  }
  html, body {
    margin: 0;
    padding: 0;
    width: 1200px;
    height: 1200px;
    overflow: hidden;
    background: var(--paper);
  }
  .canvas {
    position: relative;
    width: 1200px;
    height: 1200px;
  }
  .letterhead {
    position: absolute;
    left: 223px;
    top: 112px;
    width: 761px;
    height: 981px;
    background: var(--paper);
    border: 1px solid var(--page-edge);
    box-sizing: border-box;
    box-shadow: 7px 8px 8px rgba(0,0,0,0.28);
    overflow: hidden;
  }
  .corner-bands {
    position: absolute;
    inset: 0;
    width: 100%;
    height: 100%;
  }
  .brand-mark {
    position: absolute;
    left: 36px;
    top: 36px;
    width: 78px;
    height: 78px;
    box-sizing: border-box;
    border: 4px solid var(--brand-red);
    border-radius: 6px;
  }
  .brand-name {
    position: absolute;
    left: 130px;
    top: 34px;
    margin: 0;
    font-family: "Questrial", sans-serif;
    font-weight: 400;
    font-size: 35px;
    line-height: 40px;
    letter-spacing: 1px;
    color: var(--brand-red);
    text-transform: uppercase;
    white-space: nowrap;
  }
  .tagline {
    position: absolute;
    left: 150px;
    top: 112px;
    margin: 0;
    font-family: "Noto Serif", serif;
    font-size: 11px;
    color: var(--tagline-grey);
    letter-spacing: 0.3px;
    white-space: nowrap;
  }
  .watermark {
    position: absolute;
    left: 134px;
    top: 245px;
    width: 493px;
    height: 493px;
    box-sizing: border-box;
    border: 21px solid var(--watermark);
    border-radius: 54px;
  }
  .contact {
    position: absolute;
    right: 36px;
    top: 912px;
    margin: 0;
    font-family: "Open Sans", sans-serif;
    font-weight: 600;
    font-size: 11.5px;
    line-height: 21px;
    color: var(--brand-red);
    white-space: nowrap;
  }
  .contact p { margin: 0; }
</style>
</head>
<body>
<div class="canvas">
  <div class="letterhead">
    <svg class="corner-bands" viewBox="0 0 1218 1570" preserveAspectRatio="none" aria-hidden="true">
      <path class="band-top-right" fill="var(--brand-red)"
        d="M913,0 H1218 V620 C1196,612 1180,592 1180,566 V38 H964 C940,38 921,24 913,0 Z"/>
      <path class="rule-top-right" fill="none" stroke="var(--ink-black)" stroke-width="11"
        d="M913,0 C921,24 940,38 964,38 H1185 V566 C1185,592 1200,611 1218,619"/>
      <path class="band-bottom-left" fill="var(--brand-red)"
        d="M0,952 C22,960 38,982 38,1008 V1532 H252 C276,1532 296,1548 305,1570 H0 Z"/>
      <path class="rule-bottom-left" fill="none" stroke="var(--ink-black)" stroke-width="11"
        d="M0,953 C18,961 33,981 33,1008 V1537 H252 C276,1537 294,1551 303,1570"/>
    </svg>

    <div class="brand-mark" aria-hidden="true"></div>
    <h1 class="brand-name">Bramford<br>Holloway</h1>
    <p class="tagline">Crafted For Every Room You Love</p>

    <div class="watermark" aria-hidden="true"></div>

    <div class="contact">
      <p>Phone: +1 (555) 014-2290</p>
      <p>Email: info@bramfordhollowayinc.com</p>
    </div>
  </div>
</div>
</body>
</html>
```